i would like a business card to leave with customers and potential customers for electrical work and for the supply and install of reverse cycle airconditioning in the domestic and commercial market.
I own my own business and im a sole trader. I have an a'class electrical lisence and also a refrigeration lisence so i am
able to offer complete installations in airconditioning by a fully qualified and lisenced tradesman.
im looking for something that comes across as unique and professional.
i had the coluor black and some gold in mind but open to any coluors.
something like Brightline Electrical & Refrigeration
or Brightline Air.
i will use this design on a business card to advertise through summer to help generate installs through the busy season.

Target Market(s)

Mainly domestic house holds through summer who are in need of airconditioning and reliable information to acomadate thier cooling and heating requirements

Industry/Entity Type

Electrical

Requirements
Must have
• Business name- Brightline
My name- Peter Mulvane
My mobile no- 0438 517 209
My email- rtmulvane@kestrelnet.com.au
Installation & Decomissioning of aiconditioning split systems
LIC NO: TKR 504613
Nice to have
• Brightline Electrical & Refrigeration

```html
<!DOCTYPE html>
<html lang="en">
<head>
<meta charset="utf-8">
<title>Brightline Electrical &amp; Refrigeration – Business Card</title>
<link href="https://fonts.googleapis.com/css2?family=Open+Sans:wght@400;600;700&display=swap" rel="stylesheet">
<style>
  :root {
    --backdrop: #a33b3b;
    --navy: #17405f;
    --paper: #ffffff;
  }
  * { margin: 0; padding: 0; box-sizing: border-box; }
  html, body {
    width: 1200px;
    height: 900px;
    overflow: hidden;
    background: var(--backdrop);
    font-family: "Open Sans", Arial, sans-serif;
  }
  .card {
    position: absolute;
    left: 286px;
    width: 624px;
    height: 402px;
    border-radius: 28px;
    overflow: hidden;
  }
  .card-front {
    top: 28px;
    background: var(--paper);
  }
  .card-front .edge-band {
    position: absolute;
    top: 0;
    right: 0;
    width: 22px;
    height: 100%;
    background: var(--navy);
    border-radius: 22px 0 0 22px;
  }
  .brand {
    position: absolute;
    left: 52px;
    top: 142px;
    color: var(--navy);
  }
  .brand-name {
    font-size: 44px;
    font-weight: 700;
    letter-spacing: -1px;
    line-height: 1;
  }
  .brand-tagline {
    margin-top: 10px;
    font-size: 12px;
    font-weight: 600;
    line-height: 1;
  }
  .contact {
    position: absolute;
    right: 48px;
    top: 116px;
    text-align: right;
    color: var(--navy);
  }
  .contact-name {
    font-size: 23px;
    font-weight: 700;
    margin-bottom: 34px;
  }
  .contact-line {
    display: flex;
    justify-content: flex-end;
    align-items: center;
    gap: 10px;
    font-size: 16px;
    line-height: 28px;
  }
  .contact-line svg { width: 22px; height: 16px; fill: var(--navy); }
  .licence { margin-top: 4px; }
  .licence strong { font-weight: 700; }
  .card-back {
    top: 466px;
    background: var(--navy);
  }
  .back-wordmark {
    position: absolute;
    left: 28px;
    top: 40px;
    font-size: 120px;
    font-weight: 700;
    letter-spacing: -3px;
    line-height: 1.2;
    color: var(--paper);
    white-space: nowrap;
  }
  .back-tagline {
    position: absolute;
    left: 20px;
    bottom: 30px;
    font-size: 20px;
    color: var(--paper);
    white-space: nowrap;
  }
</style>
</head>
<body>
  <section class="card card-front">
    <div class="brand">
      <div class="brand-name">Brightline</div>
      <div class="brand-tagline">Brightline Electrical &amp; Refrigeration</div>
    </div>
    <div class="contact">
      <div class="contact-name">Peter Mulvane</div>
      <div class="contact-line">
        <span>0438 517 209</span>
        <svg viewBox="0 0 24 18" aria-hidden="true">
          <path d="M2 6c0-3 4-5 10-5s10 2 10 5v2h-5V6c-2-1-8-1-10 0v2H2z"/>
          <path d="M6 10h12l3 7H3z"/>
        </svg>
      </div>
      <div class="contact-line">
        <span>rtmulvane@kestrelnet.com.au</span>
        <svg viewBox="0 0 24 18" aria-hidden="true">
          <path d="M2 3h20v12H2z"/>
          <path d="M3 4l9 6 9-6" fill="none" stroke="#fff" stroke-width="1.4"/>
        </svg>
      </div>
      <div class="contact-line licence">
        <span>LIC NO: <strong>TKR 504613</strong></span>
      </div>
    </div>
    <div class="edge-band"></div>
  </section>

  <section class="card card-back">
    <div class="back-wordmark">Brightline</div>
    <p class="back-tagline">Installation &amp; Decomissioning of aiconditioning split systems</p>
  </section>
</body>
</html>
```